Flyer-Design für Coaching & Beratung
Zielgruppe
Coaching & Beratung in Betrieben und von Privatpersonen. Das Coaching ist Werte orientiert.
Zielgruppe: KMU (Führungskräfte) und Privatpersonen
Aufgabenstellung
Bitte Beschreibung Flyer beachten (Datei).
6-Seitiges Flyer, in quadratischer Form 10cm x 10cm

```html
<!DOCTYPE html>
<html lang="de">
<head>
<meta charset="utf-8">
<title>Lorenz Hallberg – Coaching Flyer</title>
<link href="https://fonts.googleapis.com/css2?family=Open+Sans:wght@400;600;700&display=swap" rel="stylesheet">
<style>
  :root {
    --green: #5e8138;
    --green-text: #5b8a32;
    --brown: #6b5344;
    --heading: #474d55;
    --body: #505458;
    --paper: #f6f6f6;
  }
  * { margin: 0; padding: 0; box-sizing: border-box; }
  html, body { width: 1200px; height: 400px; overflow: hidden; background: #fff; }
  .flyer {
    position: relative; width: 1200px; height: 400px; background: var(--paper);
    font-family: "Open Sans", Arial, sans-serif; color: var(--body);
  }
  .shapes { position: absolute; inset: 0; }
  .cover-menu {
    position: absolute; left: 0; width: 398px; top: 22px; text-align: center;
    list-style: none; color: #fff; font-weight: 600; font-size: 11px; line-height: 18.5px;
  }
  .brand {
    position: absolute; left: 182px; top: 162px; color: var(--brown);
    font-weight: 700; font-size: 27px; line-height: 34px; letter-spacing: 4px;
  }
  .panel-title {
    position: absolute; top: 30px; font-weight: 600; font-size: 17.5px;
    color: var(--heading); letter-spacing: 0.2px;
  }
  .topics {
    position: absolute; list-style: none; color: var(--green-text);
    font-size: 11.4px; line-height: 15px;
  }
  .topics li { position: relative; padding-left: 0; }
  .topics li::before {
    content: ""; position: absolute; left: -13px; top: 7px; width: 2.5px; height: 2.5px;
    border-radius: 50%; background: var(--green-text);
  }
  .divider { position: absolute; top: 68px; width: 1px; height: 307px; background: var(--green); }
  .copy {
    position: absolute; font-size: 11.2px; line-height: 14.9px; color: var(--body);
  }
  .copy p + p { margin-top: 14.9px; }
  .people { position: absolute; background: var(--green); border-radius: 18px 18px 4px 4px; }
</style>
</head>
<body>
<div class="flyer">
  <svg class="shapes" width="1200" height="400" viewBox="0 0 1200 400" aria-hidden="true">
    <rect x="0" y="0" width="405" height="6" fill="var(--green)"/>
    <polygon points="7,11 392,11 199,125" fill="var(--green)"/>
    <polygon points="199,304 56,390 342,390" fill="var(--green)"/>
    <polygon points="40,393 356,393 360,400 36,400" fill="var(--green)"/>
    <polygon points="475,0 529,0 502,26" fill="var(--brown)"/>
    <polygon points="917,0 970,0 943,26" fill="var(--brown)"/>
    <circle cx="87" cy="205" r="68" fill="none" stroke="var(--brown)" stroke-width="2"/>
    <line x1="182" y1="235" x2="381" y2="235" stroke="var(--brown)" stroke-width="2"/>
    <circle cx="1146" cy="349" r="30" fill="none" stroke="var(--brown)" stroke-width="1.5"/>
  </svg>

  <ul class="cover-menu">
    <li>BUSINESS COACHING</li>
    <li>PRIVATPERSONEN COACHING</li>
    <li>TELEFON &amp; ONLINECOACHING</li>
  </ul>

  <div class="brand">LORENZ<br>HALLBERG</div>

  <h2 class="panel-title" style="left:420px">BUSINESS COACHING</h2>
  <ul class="topics" style="left:435px; top:66px">
    <li>Führungskräfte Entwicklung</li>
    <li>Führungskräfte Begleitung</li>
    <li>Veränderungsprozesse</li>
    <li>Umgang mit Stress</li>
    <li>Kommunikation</li>
  </ul>
  <div class="people" style="left:420px; top:186px; width:146px; height:99px" role="img" aria-label="Grüne Silhouetten einer Gruppe von fünf Führungskräften"></div>
  <div class="divider" style="left:587px"></div>
  <div class="copy" style="left:599px; top:66px; width:200px">
    <p>Nicht nur die Fach- und Methoden-<br>kompetenz ist bei Führungskräften<br>wichtig. Im Umgang mit Mitarbei-<br>tenden ist der Führungsstiel ebenso<br>wichtig, wenn nicht sogar wichtiger.<br>Motivation, Lob und Anerkennung<br>bei Mitarbeitenden steigert deren<br>Leistung nachhaltig und somit die<br>Produktivität.</p>
    <p>Wie Führungskräfte mit Stress und<br>Veränderungen umgehen, überträgt<br>sich auf die Mitarbeiterschaft. Es<br>kann ungewollt Widerstände und<br>Demotivationen auslösen. Glaubwür-<br>dig und authentisch führen, hierbei<br>möchte ich Sie gerne unterstützen<br>und begleiten.</p>
    <p>Führung fängt bei einem selber an.<br>Wie führen Sie sich?</p>
  </div>

  <h2 class="panel-title" style="left:821px">PRIVATPERSONEN COACHING</h2>
  <ul class="topics" style="left:833px; top:69px">
    <li>Beziehungsthemen</li>
    <li>Gewohnheiten/<br>Verhalten verändern</li>
    <li>Denkblockaden lösen</li>
    <li>Berufliche Neuorientierung</li>
  </ul>
  <div class="people" style="left:868px; top:254px; width:74px; height:119px" role="img" aria-label="Grüne Silhouetten eines Mannes und einer Frau"></div>
  <div class="divider" style="left:980px"></div>
  <div class="copy" style="left:994px; top:66px; width:200px">
    <p>Manchmal meinst du etwas anders,<br>als es verstanden wird. Oder gibt<br>es vielleicht Dinge, welche dich in<br>deiner Beziehung auf die Palme<br>bringen?</p>
    <p>Vielleicht merkst du, daß dein<br>Verhalten oder deine Gewohnheiten<br>nicht immer passend sind.</p>
    <p>Wenn dir diese oder ähnliche Situa-<br>tionen bekannt vorkommen und du<br>daran etwas ändern möchtest, kön-<br>nen wir gemeinsam daran arbeiten.</p>
  </div>
</div>
</body>
</html>
```